Vexo Systems Web Site Design

Need a basic site to show clients a little about what we do. We are a custom audio video company in the high-end residential market. Need a few basic but professional pages to show past projects and products we sell. No e-commerce. Should include my new logo from ArtHivePro.

Industry/Entity Type

Residential

Number of Pages Required

2 page

Font styles to use
Serif
Sans Serif

Colors
f78f20

Requirements
Must have
• Company Logo, Send feedback page
Nice to have
• I have no ideas about design, but I do know what I like and dislike when I see it.

```html
<!DOCTYPE html>
<html lang="en">
<head>
<meta charset="utf-8">
<title>Vexo Systems</title>
<link rel="stylesheet" href="https://fonts.googleapis.com/css2?family=Jost:wght@400;500;600&family=Open+Sans:wght@400;600&display=swap">
<style>
:root{
  --accent:#f78f20;
  --accent-soft:#fde3c6;
  --ink:#1f1f1f;
  --body:#4a4a4a;
  --muted:#9a9a9a;
  --line:#e3e3e3;
  --button:#b5b5b5;
  --white:#ffffff;
}
*{box-sizing:border-box;margin:0;padding:0}
html,body{width:1200px;height:2699px;overflow:hidden}
body{position:relative;background:var(--white);font-family:"Open Sans",Arial,sans-serif;color:var(--body)}
.abs{position:absolute}
.backdrop{left:0;top:0;width:1200px;height:660px}
.brand{left:95px;top:34px;display:flex;align-items:center;gap:10px;font-family:"Jost",sans-serif;font-weight:600;font-size:20px;color:var(--ink)}
.brand-mark{width:34px;height:34px;background:var(--accent)}
.nav{right:96px;top:43px;display:flex;gap:30px;font-family:"Jost",sans-serif;font-weight:500;font-size:14px;color:var(--ink)}
.nav .current{color:var(--accent)}
.hero{left:95px;top:102px;width:1012px;height:492px;background:linear-gradient(110deg,#d9d9dc 0%,#b9b6b8 35%,#3a3535 60%,#1c1a1b 80%,#c9c3c5 100%)}
.hero-arrow{top:336px}
.hero-caption{left:124px;top:408px;width:368px;height:164px;background:rgba(20,20,20,.82);padding:26px 26px;color:var(--white)}
.hero-caption h2{font-family:"Jost",sans-serif;font-weight:500;font-size:24px;margin-bottom:6px}
.hero-caption p{font-size:12.5px;line-height:20px;width:320px}
.btn-accent{display:inline-block;margin-top:12px;background:var(--accent);color:var(--white);font-size:12px;font-weight:600;padding:5px 16px}
.section-title{left:0;width:1200px;text-align:center;font-family:"Jost",sans-serif;font-weight:500;font-size:24px;color:var(--ink)}
.intro{left:118px;top:700px;width:964px;text-align:center;font-size:10.2px;line-height:21px;color:var(--body)}
.card-img{height:159px}
.card-title{font-family:"Jost",sans-serif;font-weight:500;font-size:14px;color:var(--accent)}
.card-text{font-size:11px;line-height:21.5px;color:var(--body)}
.product-text{font-size:10.5px;line-height:17px;width:300px}
.price{font-size:17px;color:var(--muted)}
.btn-more{width:81px;height:28px;background:var(--button);color:var(--white);font-size:11px;font-weight:600;text-align:center;line-height:28px}
.projects{left:0;top:1830px;width:1200px;height:560px;background:linear-gradient(180deg,#7a4a14 0%,#b86d1a 28%,#6a4a2a 55%,#3c3a36 80%,#2e2e2e 100%)}
.project-img{left:237px;top:1940px;width:725px;height:366px;background:linear-gradient(120deg,#9fc3e3 0%,#3a78b8 45%,#183e6c 80%,#2c5c92 100%)}
.project-caption{left:237px;top:2240px;width:725px;height:66px;background:rgba(15,20,30,.82);color:var(--white);font-size:13.5px;padding:22px 28px}
.dot{top:2346px;width:12px;height:12px;border-radius:50%;background:var(--white)}
.foot-list{list-style:none;font-size:12.5px;line-height:26.5px;color:var(--body)}
.contact-row{display:flex;align-items:center;gap:32px;font-size:12.5px;color:var(--body);height:42px}
.social-row{display:flex;align-items:center;justify-content:space-between;width:132px;height:52px;font-size:12.5px;color:var(--body)}
.social-dot{width:32px;height:32px;border-radius:50%;background:var(--accent-soft);border:1.5px solid var(--accent)}
.foot-rule{left:0;top:2640px;width:1200px;height:1px;background:var(--line)}
.copyright{left:0;top:2660px;width:1200px;text-align:center;font-size:12.5px;color:var(--muted)}
</style>
</head>
<body>
<svg class="abs backdrop" viewBox="0 0 1200 660" aria-hidden="true">
  <polygon points="0,0 1200,0 1200,445 0,660" fill="#ececec"/>
  <polygon points="640,0 1200,0 1200,445 900,480" fill="#e2e2e2"/>
</svg>

<header>
  <div class="abs brand"><span class="brand-mark"></span>Vexo Systems</div>
  <nav class="abs nav">
    <span class="current">Home</span><span>About Us</span><span>Past Projects</span><span>Products</span><span>Services</span><span>Contact</span>
  </nav>
</header>

<section>
  <div class="abs hero" role="img" aria-label="Photo of high-end speakers in an audio showroom"></div>
  <svg class="abs hero-arrow" style="left:110px" width="16" height="24" viewBox="0 0 16 24" aria-hidden="true"><polyline points="12,3 4,12 12,21" fill="none" stroke="#fff" stroke-width="3"/></svg>
  <svg class="abs hero-arrow" style="left:1074px" width="16" height="24" viewBox="0 0 16 24" aria-hidden="true"><polyline points="4,3 12,12 4,21" fill="none" stroke="#fff" stroke-width="3"/></svg>
  <div class="abs hero-caption">
    <h2>Vexo Systems</h2>
    <p>We are a custom audio video company in the high-end residential market.</p>
    <span class="btn-accent">Learn More</span>
  </div>
</section>

<section>
  <h2 class="abs section-title" style="top:648px">Welcome to Vexo Systems</h2>
  <p class="abs intro">Lorem Ipsum is simply dummy text of the printing and typesetting industry. Lorem Ipsum has been the industry's standard dummy text ever since the 1500s, when an unknown printer took a galley of type and scrambled it to make a type specimen book. It has survived not only five centuries, but also the leap into electronic typesetting, remaining essentially unchanged. It was popularised in the 1960s with the release of Letraset sheets containing Lorem Ipsum passages, and more recently with desktop publishing software.</p>
</section>

<section>
  <h2 class="abs section-title" style="top:828px">Our Services</h2>
  <div class="abs card-img" style="left:95px;top:888px;width:233px;background:linear-gradient(90deg,#d8d8d8,#6a6a6a 60%,#1a1a1a)" role="img" aria-label="Close-up photo of a speaker driver"></div>
  <div class="abs card-img" style="left:353px;top:888px;width:233px;background:linear-gradient(135deg,#0c0c0c,#3a3a3a 50%,#0c0c0c)" role="img" aria-label="Photo of a video camera lens"></div>
  <div class="abs card-img" style="left:613px;top:888px;width:234px;background:linear-gradient(180deg,#5a5048,#c9c3bb 45%,#3a3430)" role="img" aria-label="Photo of a media room with a large screen"></div>
  <div class="abs card-img" style="left:873px;top:888px;width:234px;background:linear-gradient(180deg,#5b3f34,#8a6a5a 50%,#e8e6e4)" role="img" aria-label="Photo of a residential cinema wall"></div>

  <h3 class="abs card-title" style="left:95px;top:1071px">Distributed Audio</h3>
  <h3 class="abs card-title" style="left:353px;top:1071px">Distributed Video</h3>
  <h3 class="abs card-title" style="left:613px;top:1071px">Media Rooms</h3>
  <h3 class="abs card-title" style="left:873px;top:1071px">Residential Cinemas</h3>

  <p class="abs card-text" style="left:95px;top:1110px;width:232px">Lorem Ipsum is simply dummy text of the printing and typesetting industry. Lorem Ipsum has been the industry's standard dummy text ever since the 1500s, when an unknown printer took a galley .</p>
  <p class="abs card-text" style="left:353px;top:1110px;width:232px">Lorem Ipsum is simply dummy text of the printing and typesetting industry. Lorem Ipsum has been the industry's standard dummy text ever since the 1500s, when an unknown printer took a galley .</p>
  <p class="abs card-text" style="left:613px;top:1110px;width:232px">Lorem Ipsum is simply dummy text of the printing and typesetting industry. Lorem Ipsum has been the industry's standard dummy text ever since the 1500s, when an unknown printer took a galley .</p>
  <p class="abs card-text" style="left:873px;top:1110px;width:232px">Lorem Ipsum is simply dummy text of the printing and typesetting industry. Lorem Ipsum has been the industry's standard dummy text ever since the 1500s, when an unknown printer took a galley .</p>
</section>

<section>
  <h2 class="abs section-title" style="top:1304px">Our Products</h2>
  <div class="abs" style="left:95px;top:1368px;width:318px;height:216px;background:linear-gradient(120deg,#1a1c22,#3c4a5c 55%,#161616)" role="img" aria-label="Photo of an operator at a video control desk"></div>
  <div class="abs" style="left:440px;top:1368px;width:318px;height:216px;background:linear-gradient(180deg,#3d78c0,#8fb4dc 60%,#6a7a8a)" role="img" aria-label="Photo of a security camera above a city skyline"></div>
  <div class="abs" style="left:786px;top:1368px;width:318px;height:216px;background:linear-gradient(135deg,#2a2628,#6a5a56 55%,#9a7a6c)" role="img" aria-label="Photo of hands typing on a laptop"></div>

  <h3 class="abs card-title" style="left:95px;top:1602px">Audio Video</h3>
  <h3 class="abs card-title" style="left:440px;top:1602px">Camera Systems</h3>
  <h3 class="abs card-title" style="left:786px;top:1602px">Computer</h3>

  <p class="abs price" style="left:95px;top:1630px">$234.00</p>
  <p class="abs price" style="left:440px;top:1630px">$234.00</p>
  <p class="abs price" style="left:786px;top:1630px">$234.00</p>

  <p class="abs card-text product-text" style="left:95px;top:1670px">Lorem Ipsum is simply dummy text of the printing and typesetting industry. Lorem Ipsum has been the industry's standard dummy text ever</p>
  <p class="abs card-text product-text" style="left:440px;top:1670px">Lorem Ipsum is simply dummy text of the printing and typesetting industry. Lorem Ipsum has been the industry's standard dummy text ever</p>
  <p class="abs card-text product-text" style="left:786px;top:1670px">Lorem Ipsum is simply dummy text of the printing and typesetting industry. Lorem Ipsum has been the industry's standard dummy text ever</p>

  <div class="abs btn-more" style="left:95px;top:1750px">Enquire</div>
  <div class="abs btn-more" style="left:440px;top:1750px">Enquire</div>
  <div class="abs btn-more" style="left:786px;top:1750px">Enquire</div>
</section>

<section>
  <div class="abs projects" role="img" aria-label="Blurred city skyline at sunset"></div>
  <h2 class="abs section-title" style="top:1884px;color:var(--white)">Past Projects</h2>
  <div class="abs project-img" role="img" aria-label="Photo of an installed dome security camera"></div>
  <div class="abs project-caption">Neque porro quisquam est qui dolorem ipsum quia dolor sit amet, consectetur, adipisci velit...</div>
  <span class="abs dot" style="left:545px"></span>
  <span class="abs dot" style="left:569px"></span>
  <span class="abs dot" style="left:593px"></span>
  <span class="abs dot" style="left:617px"></span>
  <span class="abs dot" style="left:641px"></span>
</section>

<footer>
  <ul class="abs foot-list" style="left:95px;top:2440px">
    <li>Home</li><li>About Us</li><li>Past Projects</li><li>Products</li><li>Services</li><li>Contact</li>
  </ul>
  <ul class="abs foot-list" style="left:352px;top:2440px">
    <li>Terms &amp; Conditions</li><li>Privacy Policy</li>
  </ul>
  <div class="abs" style="left:570px;top:2433px">
    <div class="contact-row">
      <svg width="14" height="14" viewBox="0 0 14 14" aria-hidden="true"><rect x="2" y="1" width="10" height="12" rx="1" fill="none" stroke="#f78f20" stroke-width="1.6"/><line x1="4.5" y1="5" x2="9.5" y2="5" stroke="#f78f20" stroke-width="1.4"/></svg>
      <span>CT License: 0000417-X2</span>
    </div>
    <div class="contact-row">
      <svg width="14" height="14" viewBox="0 0 14 14" aria-hidden="true"><path d="M3 1 L5.5 1 L6.5 4 L5 5.2 C5.8 7 7 8.2 8.8 9 L10 7.5 L13 8.5 L13 11 C13 12 12 13 11 13 C5.5 12.5 1.5 8.5 1 3 C1 2 2 1 3 1 Z" fill="#f78f20"/></svg>
      <span>Ph:555-014-2290</span>
    </div>
    <div class="contact-row">
      <svg width="14" height="14" viewBox="0 0 14 14" aria-hidden="true"><rect x="1" y="3" width="12" height="9" fill="none" stroke="#f78f20" stroke-width="1.5"/><polyline points="1,3 7,8 13,3" fill="none" stroke="#f78f20" stroke-width="1.5"/></svg>
      <span>dana@vexosystems.example</span>
    </div>
  </div>
  <div class="abs" style="left:958px;top:2428px">
    <div class="social-row"><span>Friendly</span><span class="social-dot"></span></div>
    <div class="social-row"><span>Chirper</span><span class="social-dot"></span></div>
    <div class="social-row"><span>Linkwork</span><span class="social-dot"></span></div>
  </div>
  <div class="abs foot-rule"></div>
  <p class="abs copyright">© 2015 Vexo Systems LLC</p>
</footer>
</body>
</html>
```